Tallow Crest Software PowerPoint template

We are a software company selling endpoint visibility, access and security technology to enterprise-level IT departments.
Our technology helps organizations gain comprehensive visibility into and control over devices accessing their corporate network so they can quickly identify and address suspicious activity on the network that could lead to potential threats like data breaches.
This technology can cost organizations upwards of $1M - depending on the size of the organization. Our primary clients are Meridane 2,000 companies.
We want a professional, polished PowerPoint template that we can use for all company presentations. Please include:
Title page
Section page
General info page
Thank you page
Logo options and color specs are attached.
Please include our tagline on at least the title page: Discover the edge. Optimize the whole.

```html
<!DOCTYPE html>
<html lang="en">
<head>
<meta charset="UTF-8">
<title>Tallow Crest Software — Title Presentation</title>
<link rel="stylesheet" href="https://fonts.googleapis.com/css2?family=Fira+Sans+Condensed:wght@500;600;700&display=swap">
<style>
  :root {
    --brand-red: #8e1b1f;
    --icon-red: #9a2327;
    --accent-copper: #c7794f;
    --ring: #cf8f70;
    --rule: #b8473f;
    --bar-grey: #b3b3b3;
    --label-grey: #8a8a8a;
    --dot-tint: #ececec;
    --paper: #ffffff;
  }
  * { margin: 0; padding: 0; box-sizing: border-box; }
  html, body { width: 1200px; height: 675px; overflow: hidden; background: var(--paper); }
  .slide {
    position: relative; width: 1200px; height: 675px; overflow: hidden;
    background: var(--paper);
    font-family: "Fira Sans Condensed", "Arial Narrow", sans-serif;
  }
  .top-bar-grey { position: absolute; left: 0; top: 0; width: 960px; height: 17px; background: var(--bar-grey); }
  .top-bar-red { position: absolute; left: 960px; top: 0; width: 240px; height: 17px; background: var(--brand-red); }
  .corner-texture {
    position: absolute; left: 0; top: 17px; width: 90px; height: 170px;
    background: radial-gradient(ellipse at 20% 30%, var(--dot-tint) 0%, rgba(255,255,255,0) 70%);
  }
  .slide-title {
    position: absolute; left: 84px; top: 44px;
    font-size: 60px; font-weight: 700; letter-spacing: -0.5px;
    color: var(--brand-red); line-height: 1;
  }
  .slide-subtitle {
    position: absolute; left: 97px; top: 114px;
    font-size: 27px; font-weight: 600; color: var(--accent-copper); line-height: 1;
  }
  .feature {
    position: absolute; top: 274px; width: 180px; margin-left: -90px;
    display: flex; flex-direction: column; align-items: center;
  }
  .feature-ring {
    width: 140px; height: 140px; border-radius: 50%;
    border: 1.2px solid var(--ring);
    display: flex; align-items: center; justify-content: center;
  }
  .feature-ring svg { width: 62px; height: 62px; fill: var(--icon-red); }
  .feature-label {
    margin-top: 19px; text-align: center;
    font-size: 20px; font-weight: 600; line-height: 24px; color: var(--label-grey);
  }
  .footer-rule { position: absolute; left: 71px; top: 626px; width: 1100px; height: 1.5px; background: var(--rule); }
  .footer-brand {
    position: absolute; right: 30px; top: 640px;
    display: flex; align-items: center; gap: 8px;
  }
  .footer-brand-mark { width: 12px; height: 12px; border-radius: 50%; background: var(--rule); }
  .footer-brand-name {
    font-size: 13px; font-weight: 600; letter-spacing: 1.5px;
    color: var(--brand-red); text-transform: uppercase;
  }
</style>
</head>
<body>
<main class="slide">
  <div class="top-bar-grey"></div>
  <div class="top-bar-red"></div>
  <div class="corner-texture" role="img" aria-label="Faint dotted texture in the top-left corner"></div>

  <h1 class="slide-title">TITLE PRESENTATION</h1>
  <p class="slide-subtitle">Subtitle Presentation</p>

  <section class="feature" style="left:210px">
    <div class="feature-ring">
      <svg viewBox="0 0 64 64" aria-hidden="true">
        <ellipse cx="32" cy="38" rx="12" ry="15"/>
        <circle cx="32" cy="20" r="7"/>
        <g stroke="var(--icon-red)" stroke-width="3" stroke-linecap="round">
          <line x1="27" y1="14" x2="23" y2="8"/><line x1="37" y1="14" x2="41" y2="8"/>
          <line x1="20" y1="30" x2="10" y2="26"/><line x1="44" y1="30" x2="54" y2="26"/>
          <line x1="19" y1="38" x2="8" y2="38"/><line x1="45" y1="38" x2="56" y2="38"/>
          <line x1="21" y1="47" x2="11" y2="53"/><line x1="43" y1="47" x2="53" y2="53"/>
        </g>
      </svg>
    </div>
    <p class="feature-label">Lorem<br>Ipsum</p>
  </section>

  <section class="feature" style="left:401px">
    <div class="feature-ring">
      <svg viewBox="0 0 64 64" aria-hidden="true">
        <path d="M14 6 a10 10 0 0 0 -6 14 l30 30 a5 5 0 0 0 8 -8 l-30 -30 a10 10 0 0 0 -14 -6 l6 6 -2 6 -6 2 z" transform="translate(6 6)"/>
        <path d="M50 6 l8 8 -6 4 -18 18 -4 -4 18 -18 z"/>
        <path d="M28 38 l-16 16 a4 4 0 0 0 6 6 l16 -16 z"/>
      </svg>
    </div>
    <p class="feature-label">Lorem<br>Ipsum</p>
  </section>

  <section class="feature" style="left:600px">
    <div class="feature-ring">
      <svg viewBox="0 0 64 64" aria-hidden="true">
        <path d="M32 4 C22 10 14 10 8 10 C8 36 16 52 32 60 C48 52 56 36 56 10 C50 10 42 10 32 4 Z"/>
        <path d="M32 10 C24 14 18 15 13 15 C13 22 14 28 16 33 H32 Z" fill="#fff"/>
        <path d="M32 33 H48 C46 42 40 50 32 55 Z" fill="#fff"/>
      </svg>
    </div>
    <p class="feature-label">Lorem<br>Ipsum</p>
  </section>

  <section class="feature" style="left:791px">
    <div class="feature-ring">
      <svg viewBox="0 0 64 64" aria-hidden="true">
        <rect x="8" y="28" width="10" height="26" rx="2"/>
        <path d="M22 28 L32 12 C34 8 40 9 39 14 L37 24 H52 C56 24 58 28 56 31 C58 33 58 37 55 39 C57 41 56 45 53 46 C55 49 52 53 48 53 H22 Z"/>
      </svg>
    </div>
    <p class="feature-label">Lorem<br>Ipsum</p>
  </section>

  <section class="feature" style="left:980px">
    <div class="feature-ring">
      <svg viewBox="0 0 64 64" aria-hidden="true">
        <path d="M24 8 L40 8 L36 18 L28 18 Z"/>
        <path d="M27 20 H37 C50 28 56 40 54 50 C52 58 44 60 32 60 C20 60 12 58 10 50 C8 40 14 28 27 20 Z"/>
        <text x="32" y="50" text-anchor="middle" font-size="22" font-weight="700" fill="#fff" font-family="Fira Sans Condensed, sans-serif">$</text>
      </svg>
    </div>
    <p class="feature-label">Lorem<br>Ipsum</p>
  </section>

  <div class="footer-rule"></div>
  <div class="footer-brand">
    <span class="footer-brand-mark"></span>
    <span class="footer-brand-name">Tallow Crest Software</span>
  </div>
</main>
</body>
</html>
```